Lantern Vale Photography business card design required

Needing business card made up for my new photography business.

Target Market(s)

Target will mostly be regular people with the occasional industrial or commercial customer.

Industry/Entity Type

Business

Font styles to use
Sans Serif

Colors

Designer to choose colors to be used in the design.

Requirements
Must have
• Morgan Tillbrook
Ph: 0437 262 508
Email: info@lanternvalephoto.example
Web: www.lanternvalephoto.example

On the back possibly links for social media including Facebook, Flickr and Instagram (links to be determined).

```html
<!DOCTYPE html>
<html lang="en">
<head>
<meta charset="utf-8">
<title>Lantern Vale Photography – Business Card</title>
<link rel="stylesheet" href="https://fonts.googleapis.com/css2?family=Cinzel:wght@400;700&display=swap">
<style>
  :root {
    --page-bg: #e4e2df;
    --frost-light: #f4f4f3;
    --frost-mid: #dcdcdb;
    --frost-warm: #e6d9da;
    --panel-dark: #0d0c0b;
    --panel-deep: #1d1b19;
    --brand-grey: #3b3b3b;
    --accent-blue: #1f6c9e;
    --name-brown: #7a5b3c;
    --detail-brown: #8a7458;
  }
  * { margin: 0; padding: 0; box-sizing: border-box; }
  html, body {
    width: 1200px;
    height: 970px;
    overflow: hidden;
    background: var(--page-bg);
  }
  .card {
    position: absolute;
    left: 100px;
    top: 207px;
    width: 1000px;
    height: 556px;
    display: flex;
    box-shadow: 0 18px 40px rgba(0,0,0,0.18);
    font-family: "Cinzel", serif;
  }
  .card-front {
    width: 470px;
    height: 100%;
    background: linear-gradient(170deg, var(--frost-light) 0%, var(--frost-mid) 55%, var(--frost-warm) 78%, var(--frost-mid) 100%);
    display: flex;
    align-items: center;
    justify-content: center;
    gap: 18px;
  }
  .brand-mark {
    width: 64px;
    height: 64px;
    border-radius: 50%;
    border: 10px solid var(--accent-blue);
    flex: none;
  }
  .brand-name {
    color: var(--brand-grey);
    font-weight: 700;
    font-size: 30px;
    line-height: 1.15;
    width: 260px;
  }
  .card-back {
    width: 530px;
    height: 100%;
    background: linear-gradient(180deg, var(--panel-dark) 0%, var(--panel-deep) 60%, var(--panel-dark) 100%);
    padding: 128px 0 0 36px;
    font-variant: small-caps;
  }
  .holder-name {
    color: var(--name-brown);
    font-weight: 700;
    font-size: 27px;
    letter-spacing: 0.5px;
  }
  .holder-role {
    color: var(--accent-blue);
    font-size: 21px;
    margin-top: -2px;
  }
  .contact-list { list-style: none; margin-top: 34px; }
  .contact-list li {
    color: var(--detail-brown);
    font-size: 21px;
    line-height: 34px;
    letter-spacing: 0.4px;
  }
  .contact-label { color: var(--accent-blue); font-weight: 700; margin-right: 6px; }
  .web-link {
    color: var(--accent-blue);
    font-size: 21px;
    margin-top: 30px;
    letter-spacing: 0.4px;
  }
  .social-row {
    display: flex;
    align-items: center;
    margin-top: 52px;
    gap: 8px;
  }
  .social-slot {
    width: 22px;
    height: 22px;
    background: var(--accent-blue);
    border-radius: 3px;
  }
  .social-cta {
    color: var(--name-brown);
    font-size: 21px;
    margin-left: 34px;
  }
</style>
</head>
<body>
  <section class="card">
    <div class="card-front">
      <span class="brand-mark"></span>
      <span class="brand-name">Lantern Vale Photography</span>
    </div>
    <div class="card-back">
      <h1 class="holder-name">Morgan Tillbrook</h1>
      <p class="holder-role">Photographer</p>
      <ul class="contact-list">
        <li><span class="contact-label">P:</span>0437 262 508</li>
        <li><span class="contact-label">E:</span>info@lanternvalephoto.example</li>
      </ul>
      <p class="web-link">www.lanternvalephoto.example</p>
      <div class="social-row">
        <span class="social-slot"></span>
        <span class="social-slot"></span>
        <span class="social-slot"></span>
        <span class="social-cta">Contact Me</span>
      </div>
    </div>
  </section>
</body>
</html>
```